Brochure and business Design Project

I need to designee brochures for my company and need material helps me to market my business.
I own a corporate housing company and accommodations services which is we rent out furnished apartment for short term lease 30 days or more and we provider many services for international patient who come to Houston Brightwater medical center for medical treatment , pleasure , business or visit we also provide help with limousine service airport pick ups , cleaning services , concierge service , car rental services , prepaid services , immigration stay extend service .
explain about services we provide and talk about our goal and the company, i need inviting colors we accommodating people like hotline and etc, my logo must be change to fit with new design, i do not want to copy and past what i have on my website or on what i sent i need better story and something to help me marking my hosting business

Target Market(s)

business material

Industry/Entity Type

Accommodation

Colors

Designer to choose colors to be used in the design.

Requirements
Must have
• explain about services we provide and talk about our goal and the company, i need inviting colors we accommodating people like hotline and etc, my logo must be change to fit with new design, i do not want to copy and past what i have on my website or on what i sent i need better story and something to help me marking my business . we accommodate patient from all over the planet who comes for medicl treatment at Brightwater medical center
Nice to have
• different langue's
Should not have
• any sexual , or religion signs

```html
<!DOCTYPE html>
<html lang="en">
<head>
<meta charset="utf-8">
<title>Harborline Suites – Corporate Housing Flyer</title>
<link href="https://fonts.googleapis.com/css2?family=Crimson+Text:wght@400;600;700&family=Libre+Baskerville:wght@700&display=swap" rel="stylesheet">
<style>
  :root {
    --pink: #d8134f;
    --ink: #1f1f1f;
    --black: #141414;
    --paper: #ffffff;
    --stage: #e4e4e4;
  }
  * { margin: 0; padding: 0; box-sizing: border-box; }
  html, body { width: 1200px; height: 2273px; overflow: hidden; }
  body { background: var(--stage); font-family: "Crimson Text", Georgia, serif; color: var(--ink); }

  .flyer {
    position: absolute; left: 50px; top: 363px;
    width: 1100px; height: 1546px;
    background: var(--paper);
    box-shadow: 0 10px 30px rgba(0,0,0,.25);
    overflow: hidden;
  }
  .abs { position: absolute; }

  .hero-photo { position: absolute; left: 0; top: 0; width: 1100px; height: 432px; }
  .corner-block { position: absolute; left: 0; top: 228px; width: 240px; height: 342px; }

  .brand { left: 62px; top: 150px; display: flex; align-items: center; gap: 10px;
    font-size: 34px; font-weight: 600; color: var(--pink); letter-spacing: .3px; }
  .brand-dot { width: 14px; height: 14px; background: var(--pink); }

  .title-main { left: 198px; top: 445px; width: 870px; text-align: center;
    font-family: "Libre Baskerville", Georgia, serif; font-weight: 700;
    font-size: 52px; line-height: 64px; color: var(--pink); letter-spacing: 1px; }
  .title-sub { left: 198px; top: 515px; width: 870px; text-align: center;
    font-family: "Libre Baskerville", Georgia, serif; font-weight: 700;
    font-size: 56px; line-height: 68px; letter-spacing: 1px;
    background: linear-gradient(180deg, #9a9a9a 0%, #2a2a2a 55%, #7a7a7a 100%);
    -webkit-background-clip: text; background-clip: text; color: transparent; }

  .section-head { font-size: 29px; font-weight: 700; color: var(--pink); letter-spacing: .5px;
    border-bottom: 2px solid var(--pink); line-height: 1.1; }
  .story-head { left: 47px; top: 604px; }
  .story-sub { left: 47px; top: 645px; font-size: 20px; line-height: 26px; font-weight: 700; }
  .story-text { left: 47px; top: 674px; width: 1010px; font-size: 15.5px; line-height: 19.5px; }
  .story-text .wrap-top { float: right; width: 0; height: 30px; }
  .story-text .wrap-gap { float: right; clear: right; width: 340px; height: 150px; }
  .story-photo { left: 732px; top: 693px; width: 368px; height: 178px; }

  .amenities-head { left: 47px; top: 900px; }
  .amenity { width: 280px; text-align: center; font-size: 15px; line-height: 19px; }
  .amenity svg { display: block; margin: 0 auto 2px; width: 30px; height: 30px; }
  .amenity h3 { font-size: 18px; font-weight: 700; line-height: 22px; }
  .amenity .icon { fill: var(--pink); stroke: var(--pink); }
  .col-1 { left: 0; } .col-2 { left: 267px; } .col-3 { left: 522px; width: 300px; } .col-4 { left: 822px; }
  .row-1 { top: 938px; } .row-2 { top: 1074px; } .row-3 { top: 1216px; }

  .contact { left: 794px; top: 1211px; width: 306px; height: 204px; }
  .contact-body { left: 830px; top: 1222px; width: 262px; color: #fff; font-size: 15px; line-height: 20px; }
  .contact-body h2 { font-size: 25px; font-weight: 700; text-align: center; text-decoration: underline;
    text-underline-offset: 4px; margin-bottom: 6px; line-height: 30px; }
  .contact-row { display: flex; gap: 10px; align-items: flex-start; }
  .contact-row svg { width: 13px; height: 13px; margin-top: 4px; flex: none; fill: #fff; }

  .map { left: 794px; top: 1415px; width: 306px; height: 115px; }

  .goal-head { left: 47px; top: 1366px; }
  .goal-text { left: 47px; top: 1403px; width: 700px; font-size: 15px; line-height: 19.5px; }

  .foot-bar { left: 0; top: 1530px; width: 1100px; height: 16px; background: var(--pink); }
</style>
</head>
<body>
<main class="flyer">

  <svg class="hero-photo" viewBox="0 0 1100 432" role="img" aria-label="Photograph of a downtown city skyline at dusk with lit office towers">
    <defs>
      <linearGradient id="skyline" x1="0" y1="0" x2="0" y2="1">
        <stop offset="0" stop-color="#4a55c8"/>
        <stop offset=".45" stop-color="#5b3f7a"/>
        <stop offset="1" stop-color="#c27a88"/>
      </linearGradient>
    </defs>
    <polygon points="435,0 1100,0 1100,432 198,432" fill="url(#skyline)"/>
  </svg>

  <svg class="corner-block" viewBox="0 0 240 342" aria-hidden="true">
    <polygon points="0,0 240,0 240,18 206,82 206,342 0,342" fill="var(--pink)"/>
    <polygon points="0,6 226,6 190,74 190,342 0,342" fill="var(--black)"/>
    <rect x="0" y="0" width="18" height="342" fill="var(--pink)"/>
    <rect x="18" y="0" width="222" height="6" fill="#fff"/>
  </svg>

  <div class="abs brand"><span class="brand-dot"></span>harborline suites</div>

  <h1 class="abs title-main">HARBORLINE SUITES</h1>
  <div class="abs title-sub">CORPORATE HOUSING</div>

  <h2 class="abs section-head story-head">OUR STORY</h2>
  <div class="abs story-sub">With a History in Business and Service</div>
  <p class="abs story-text"><span class="wrap-top"></span><span class="wrap-gap"></span>Sam Rahal (founder), started Harborline Suites in 2011. His intention was to help people who come from all over the world to the Brightwater Medical Center. Since he was managing a family business in the medical center, he came in contact with a lot of people, and many would ask him about different things in the Houston area, from where to find furnished apartments, to places to eat, or places to go to. A very sociable person who loves to meet and help people out. Today, Sam has created multiple locations of his business, and has done a wonderful job of helping people within the Houston Area. Nadia Rahal (the other founder and Sam's sister, a mother of two girls and a boy), dedicates her time to help out clients who come through Harborline Suites. As family business, they work together to provide 100% customer satisfaction. Harborline Suites focus is to provide great housing, with comfortable stay in the Houston area. Whether finding a furnished apartment, a car rental, or even if you are looking to ship a package outside the US, Harborline Suites will do their best to find a solution to help you out.</p>
  <svg class="abs story-photo" viewBox="0 0 368 178" role="img" aria-label="Photograph of a traveller looking over a night city">
    <defs>
      <linearGradient id="night" x1="0" y1="0" x2="1" y2="1">
        <stop offset="0" stop-color="#3d4a5c"/>
        <stop offset="1" stop-color="#1b2230"/>
      </linearGradient>
    </defs>
    <polygon points="48,0 368,0 368,178 0,178" fill="url(#night)"/>
  </svg>

  <h2 class="abs section-head amenities-head">AMENITIES</h2>

  <div class="abs amenity col-1 row-1">
    <svg class="icon" viewBox="0 0 34 34"><path d="M4 14a18 18 0 0 1 26 0M8 19a12 12 0 0 1 18 0M12 24a6 6 0 0 1 10 0" fill="none" stroke-width="3" stroke-linecap="round"/><circle cx="17" cy="28" r="2.5" stroke="none"/></svg>
    <h3>Internet</h3>WiFi is available in the<br>hotel rooms and is free of charge.
  </div>
  <div class="abs amenity col-2 row-1">
    <svg class="icon" viewBox="0 0 34 34"><rect x="3" y="4" width="20" height="26" rx="3" fill="none" stroke-width="3"/><path d="M10 24V11h5a4 4 0 0 1 0 8h-5" fill="none" stroke-width="3"/><rect x="26" y="6" width="5" height="24" stroke="none"/></svg>
    <h3>Parking</h3>Free private parking is<br>available on site (reservation is not needed).
  </div>
  <div class="abs amenity col-3 row-1">
    <svg class="icon" viewBox="0 0 34 34" stroke="none"><circle cx="9" cy="12" r="3.5"/><circle cx="17" cy="8" r="3.5"/><circle cx="25" cy="12" r="3.5"/><ellipse cx="17" cy="23" rx="7" ry="6"/></svg>
    <h3>Pets</h3>Pets are allowed on<br>request. Charges may apply.
  </div>
  <div class="abs amenity col-4 row-1">
    <svg class="icon" viewBox="0 0 34 34"><path d="M3 22q3.5-4 7 0t7 0 7 0 7 0M3 28q3.5-4 7 0t7 0 7 0 7 0" fill="none" stroke-width="2.5"/><circle cx="24" cy="9" r="3.5" stroke="none"/></svg>
    <h3>Pool</h3>Outdoor Pool – FREE<br>Outdoor Pool (seasonal) – FREE
  </div>

  <div class="abs amenity col-1 row-2">
    <svg class="icon" viewBox="0 0 34 34"><path d="M8 4v26M4 4v8a4 4 0 0 0 8 0V4M26 4c-4 2-5 8-5 14h5v12" fill="none" stroke-width="2.5" stroke-linecap="round"/></svg>
    <h3>Food &amp; Drink</h3>BBQ Facilities
  </div>
  <div class="abs amenity col-2 row-2">
    <svg class="icon" viewBox="0 0 34 34" stroke="none"><rect x="4" y="10" width="7" height="20" rx="2"/><rect x="13.5" y="16" width="7" height="14" rx="2"/><rect x="23" y="10" width="7" height="20" rx="2"/><circle cx="7.5" cy="5" r="3"/><circle cx="17" cy="11" r="3"/><circle cx="26.5" cy="5" r="3"/></svg>
    <h3>Family Friendly</h3>Free private parking is<br>available on site (reservation is<br>not needed).
  </div>
  <div class="abs amenity col-3 row-2">
    <svg class="icon" viewBox="0 0 34 34"><circle cx="17" cy="17" r="14" stroke="none"/><rect x="15" y="14" width="4" height="12" fill="#fff" stroke="none"/><circle cx="17" cy="9.5" r="2.3" fill="#fff" stroke="none"/></svg>
    <h3>General</h3>Non-smoking Rooms<br>Air Conditioning – FREE<br>All Spaces Non-Smoking (public and private)<br>Elevator, Heating, Grounds, Terrace
  </div>
  <div class="abs amenity col-4 row-2">
    <svg class="icon" viewBox="0 0 34 34"><path d="M17 3v8M17 23v8M3 17h8M23 17h8M7 7l5 5M22 22l5 5M27 7l-5 5M12 22l-5 5" fill="none" stroke-width="2.5" stroke-linecap="round"/></svg>
    <h3>Spa &amp; Wellness</h3>Fitness Center – FREE
  </div>

  <div class="abs amenity col-1 row-3">
    <svg class="icon" viewBox="0 0 34 34"><rect x="5" y="3" width="24" height="24" rx="4" stroke="none"/><rect x="8" y="7" width="18" height="9" fill="#fff" stroke="none"/><circle cx="11" cy="21" r="2" fill="#fff" stroke="none"/><circle cx="23" cy="21" r="2" fill="#fff" stroke="none"/><rect x="7" y="27" width="4" height="4" stroke="none"/><rect x="23" y="27" width="4" height="4" stroke="none"/></svg>
    <h3>Transportation</h3>Airport Shuttle<br>Airport Shuttle (additional charge)<br>Car Rental
  </div>
  <div class="abs amenity col-2 row-3">
    <svg class="icon" viewBox="0 0 34 34"><circle cx="17" cy="17" r="12" fill="none" stroke-width="3"/><path d="M17 5v24M5 17h24" fill="none" stroke-width="2"/></svg>
    <h3>Activities</h3>Pool Table – FREE
  </div>
  <div class="abs amenity col-3 row-3">
    <svg class="icon" viewBox="0 0 34 34"><path d="M22 3l-8 18" fill="none" stroke-width="3" stroke-linecap="round"/><path d="M8 20h14l3 11H5z" stroke="none"/></svg>
    <h3>Cleaning Services</h3>Laundry
  </div>

  <svg class="abs contact" viewBox="0 0 306 204" aria-hidden="true">
    <polygon points="0,0 306,0 306,204 28,204 0,172" fill="var(--pink)"/>
  </svg>
  <div class="abs contact-body">
    <h2>Contact</h2>
    <div class="contact-row"><svg viewBox="0 0 24 24"><path d="M6 2l4 5-2.5 2.5a14 14 0 0 0 7 7L17 14l5 4-2 4C11 22 2 13 2 4z"/></svg><span style="font-size:18px;font-weight:700">+18325550147</span></div>
    <div class="contact-row"><svg viewBox="0 0 24 24"><path d="M2 5h20v14H2zM2 5l10 8 10-8" fill="none" stroke="#fff" stroke-width="2"/></svg><span>hello@harborlinesuites.com</span></div>
    <div class="contact-row"><svg viewBox="0 0 24 24"><circle cx="12" cy="12" r="10"/></svg><span>www.harborlinesuites.com</span></div>
    <div class="contact-row" style="margin-top:6px"><svg viewBox="0 0 24 24"><path d="M12 1a8 8 0 0 0-8 8c0 6 8 14 8 14s8-8 8-14a8 8 0 0 0-8-8zm0 11a3 3 0 1 1 0-6 3 3 0 0 1 0 6z"/></svg><span>Lindenfield Drive<br>Houston ,TX 77099<br>United States of America</span></div>
  </div>

  <svg class="abs map" viewBox="0 0 306 115" role="img" aria-label="Street map showing the office location">
    <rect width="306" height="115" fill="#e9ecef"/>
  </svg>

  <h2 class="abs section-head goal-head">OUR GOAL</h2>
  <p class="abs goal-text">Lorem Ipsum is simply dummy text of the printing and typesetting industry. Lorem Ipsum has been the industry's standard dummy text ever since the 1500s, when an unknown printer took a galley of type and scrambled it to make a type specimen book. It has survived not only five centuries, but also the leap into electronic typesetting, remaining essentially unchanged. It was popularised in the 1960s with the release of Lettrex sheets containing Lorem Ipsum passages, and more recently with desktop publishing of Lorem Ipsum.</p>

  <div class="abs foot-bar"></div>
</main>
</body>
</html>
```